Velno Recycling needs a new web design

We need a new web design for our company based in Austin, TX. We resell and recycling electronics such as laptops, computer components, Tovlets, Brunos, etc. Since our inception over ten years ago, we’ve become one of the premier electronics recycling and remarketing companies in Austin, Texas.

```html
<!DOCTYPE html>
<html lang="en">
<head>
<meta charset="utf-8">
<title>Velno Recycling</title>
<link href="https://fonts.googleapis.com/css2?family=Raleway:wght@400;500;600;700&display=swap" rel="stylesheet">
<style>
:root{
  --page:#f1f2f4;
  --blue:#1b72c2;
  --blue-deep:#135a9c;
  --sky:#2fa8f2;
  --ink:#1c2633;
  --wood-1:#6b4630;
  --wood-2:#4a2f1f;
  --wood-3:#2e1c12;
  --white:#ffffff;
  --soft:#e2d9d2;
}
*{margin:0;padding:0;box-sizing:border-box}
html,body{width:1200px;height:1200px;overflow:hidden;background:var(--page);font-family:"Raleway",sans-serif}
.site{position:absolute;left:0;top:232px;width:1200px;height:736px;background:var(--white);overflow:hidden}
.header{position:absolute;left:0;top:0;width:1200px;height:96px;background:linear-gradient(100deg,#1e6fb8 0%,#2a83cf 45%,#1a64a8 100%)}
.logo-box{position:absolute;left:183px;top:0;width:264px;height:106px;background:var(--white);box-shadow:0 2px 8px rgba(0,0,0,.25);display:flex;align-items:center;justify-content:center;gap:10px;z-index:3}
.logo-dot{width:30px;height:30px;border-radius:50%;background:var(--blue)}
.logo-name{font-weight:700;font-size:24px;color:var(--blue);letter-spacing:.2px}
.contact-bar{position:absolute;left:569px;top:0;width:458px;height:29px;background:var(--ink);border-radius:0 0 8px 8px;display:flex;align-items:center;padding:0 18px;gap:14px;font-size:11px;color:#cfd8e3}
.contact-bar .item{display:flex;align-items:center;gap:6px;white-space:nowrap}
.contact-bar .sep{width:1px;height:16px;background:#4a5868}
.social{display:flex;gap:16px;margin-left:auto}
.social span{width:8px;height:8px;border-radius:50%;background:#e6edf5}
.nav{position:absolute;left:0;top:49px;width:1200px;height:29px}
.nav a{position:absolute;top:8px;font-size:10.5px;font-weight:700;color:var(--white);text-decoration:none;letter-spacing:.2px;white-space:nowrap}
.nav .home{left:627px}
.nav .about{left:679px}
.nav .services-link{left:741px}
.nav .contact{left:813px}
.nav .cta{left:897px;top:0;width:130px;height:29px;border-radius:15px;background:var(--sky);display:flex;align-items:center;justify-content:center}
.hero{position:absolute;left:0;top:96px;width:1200px;height:523px;background:radial-gradient(ellipse at 50% 45%,var(--wood-1) 0%,var(--wood-2) 55%,var(--wood-3) 100%)}
.hero-copy{position:absolute;left:0;top:0;width:1200px;text-align:center;color:var(--white)}
.kicker{position:absolute;left:0;width:1200px;top:85px;font-size:35px;font-weight:400;letter-spacing:.5px}
.headline{position:absolute;left:0;width:1200px;top:126px;font-size:68px;font-weight:400;letter-spacing:1px;line-height:1}
.banner{position:absolute;left:389px;top:204px;width:429px;height:31px;background:var(--blue);font-size:16.5px;font-weight:700;display:flex;align-items:center;justify-content:center;letter-spacing:.2px}
.intro{position:absolute;left:400px;top:248px;width:407px;font-size:12.5px;line-height:19px;color:var(--soft)}
.btn{position:absolute;top:329px;height:34px;font-size:10.5px;font-weight:700;display:flex;align-items:center;justify-content:center;color:var(--white)}
.btn.solid{left:490px;width:98px;background:var(--blue)}
.btn.ghost{left:610px;width:143px;border:1.5px solid var(--white)}
.services{position:absolute;left:0;top:0;width:1200px;height:736px;pointer-events:none}
.service{position:absolute;top:521px;width:175px;height:175px;border-radius:50%;background:var(--blue);box-shadow:0 4px 10px rgba(0,0,0,.2);display:flex;flex-direction:column;align-items:center;justify-content:center;color:var(--white)}
.service svg{width:72px;height:72px;margin-top:-8px}
.service span{margin-top:14px;font-size:12.5px;font-weight:700;letter-spacing:.3px}
</style>
</head>
<body>
<main class="site">
  <header class="header" role="img" aria-label="Blue-tinted photo of circuit boards behind the header"></header>
  <div class="logo-box"><span class="logo-dot"></span><span class="logo-name">Velno Recycling</span></div>
  <div class="contact-bar">
    <div class="item">
      <svg width="11" height="11" viewBox="0 0 12 12"><circle cx="6" cy="6" r="5" fill="none" stroke="#2fa8f2" stroke-width="1.3"/><circle cx="6" cy="6" r="2" fill="none" stroke="#2fa8f2" stroke-width="1.3"/></svg>
      mara@velnorecycling.com
    </div>
    <span class="sep"></span>
    <div class="item">
      <svg width="11" height="11" viewBox="0 0 12 12"><path d="M2 1.5l2.2-.3 1 2.4-1.3 1a6 6 0 0 0 3.5 3.5l1-1.3 2.4 1-.3 2.2C6 10 2 6 2 1.5z" fill="none" stroke="#2fa8f2" stroke-width="1.1"/></svg>
      (512) 555-0142
    </div>
    <span class="sep"></span>
    <div class="social"><span></span><span></span><span></span></div>
  </div>
  <nav class="nav">
    <a class="home">HOME</a>
    <a class="about">ABOUT</a>
    <a class="services-link">SERVICES</a>
    <a class="contact">CONTACT US</a>
    <a class="cta">SCHEDULE A PICKUP</a>
  </nav>
  <section class="hero" role="img" aria-label="Top-down photo of computer parts on a dark wooden desk">
    <div class="hero-copy">
      <div class="kicker">COMPUTER RECYCLING</div>
      <h1 class="headline">MADE EASY</h1>
      <div class="banner">MAKE A DIFFERENCE TO OUR ENVIRONMENT</div>
      <p class="intro">Want to make a difference to our environment and planet? Velno Recycling is here to help! Velno recycling has been helping keep the environment healthy since 2006, we specialize in recycling ...</p>
      <a class="btn solid">READ MORE</a>
      <a class="btn ghost">SCHEDULE A PICKUP</a>
    </div>
  </section>
  <div class="services">
    <div class="service" style="left:184px">
      <svg viewBox="0 0 72 72" fill="none" stroke="#fff" stroke-width="2.2" stroke-linejoin="round"><rect x="10" y="30" width="34" height="22"/><path d="M44 36h10l8 9v7H44z"/><rect x="14" y="20" width="12" height="10"/><rect x="28" y="20" width="12" height="10"/><rect x="21" y="8" width="12" height="12"/><circle cx="18" cy="56" r="4.5"/><circle cx="30" cy="56" r="4.5"/><circle cx="54" cy="56" r="4.5"/></svg>
      <span>LOGISTICS</span>
    </div>
    <div class="service" style="left:405px">
      <svg viewBox="0 0 72 72" fill="none" stroke="#fff" stroke-width="2.4" stroke-linecap="round" stroke-linejoin="round"><path d="M56 30a22 22 0 0 0-38-10"/><path d="M16 12v9h9"/><path d="M16 42a22 22 0 0 0 38 10"/><path d="M56 60v-9h-9"/></svg>
      <span>RECYCLING</span>
    </div>
    <div class="service" style="left:619px">
      <svg viewBox="0 0 72 72" fill="none" stroke="#fff" stroke-width="2.2" stroke-linejoin="round"><rect x="22" y="10" width="22" height="18"/><rect x="8" y="30" width="26" height="22"/><rect x="34" y="30" width="18" height="22"/><circle cx="54" cy="46" r="12"/><path d="M48 44a7 7 0 0 1 12-2M60 48a7 7 0 0 1-12 2" stroke-linecap="round"/></svg>
      <span>RETURN</span>
    </div>
    <div class="service" style="left:840px">
      <svg viewBox="0 0 72 72" fill="none" stroke="#fff" stroke-width="2.2" stroke-linejoin="round"><rect x="6" y="8" width="60" height="46"/><rect x="11" y="13" width="50" height="36"/><rect x="17" y="19" width="14" height="10"/><path d="M36 21h18M36 27h18M17 36h22"/><circle cx="52" cy="44" r="7"/><path d="M47 50l-2 10 7-4 7 4-2-10"/></svg>
      <span>CERTIFICATES</span>
    </div>
  </div>
</main>
</body>
</html>
```